The design should be a multi-page, foldable flyer with the logo and the product name on the front and the web address on the back.
MuLOTI is a word play on "zebra", which the design should reflect in some way.

Target Market(s)

Schools and individual teachers

Industry/Entity Type

Product

Colors
ffffff
000000

```html
<!DOCTYPE html>
<html lang="en">
<head>
<meta charset="utf-8">
<title>MuLOTI – Bifold Flyer</title>
<link href="https://fonts.googleapis.com/css2?family=Arimo:wght@400;700&family=Oswald:wght@300;400;600&family=Lato:wght@400;700&display=swap" rel="stylesheet">
<style>
  :root {
    --red: #d40f14;
    --red-dark: #a80a0e;
    --black: #1c1c1c;
    --ink: #141414;
    --white: #ffffff;
    --paper: #f1f1f1;
    --paper-shade: #d9d9d9;
    --stage: #ececec;
    --grey-text: #5a5a5a;
  }
  * { box-sizing: border-box; margin: 0; padding: 0; }
  html, body { width: 1200px; height: 1200px; overflow: hidden; }
  body { background: var(--stage); position: relative; font-family: "Lato", sans-serif; }

  .flyer {
    position: absolute; left: 70px; top: 225px;
    width: 1060px; height: 750px;
    display: flex;
    box-shadow: 0 6px 18px rgba(0,0,0,.25);
  }
  .panel { position: relative; width: 530px; height: 750px; overflow: hidden; }
  .panel svg.shapes { position: absolute; inset: 0; width: 100%; height: 100%; }

  /* Back panel */
  .back { background: linear-gradient(180deg, var(--paper) 0%, #e2e2e2 60%, var(--paper-shade) 100%); }
  .back .title {
    position: absolute; top: 52px; width: 100%; text-align: center;
    font-family: "Arimo", sans-serif; font-weight: 700; font-size: 50px; color: var(--ink); letter-spacing: 1px;
  }
  .back .tagline {
    position: absolute; top: 104px; width: 100%; text-align: center;
    font-family: "Arimo", sans-serif; font-weight: 700; font-size: 21px; line-height: 27px;
  }
  .back .tagline .red { color: var(--red); display: block; }
  .back .tagline .dark { color: var(--ink); display: block; }
  .back .intro {
    position: absolute; top: 184px; left: 28px; right: 28px; text-align: center;
    font-size: 11.5px; line-height: 14px; color: var(--ink);
  }
  .back .wordcloud {
    position: absolute; left: 160px; top: 258px; width: 200px; height: 160px;
    background: radial-gradient(ellipse at center, #d8242a 0%, #c9a56a 55%, rgba(200,200,200,.4) 100%);
    opacity: .85; border-radius: 4px;
  }
  .back .brand {
    position: absolute; top: 588px; width: 100%; text-align: center;
    font-family: "Arimo", sans-serif; font-weight: 400; font-size: 32px; color: var(--white); letter-spacing: 1px;
  }
  .back .brand .dot { display: inline-block; width: 14px; height: 14px; border-radius: 50%; background: var(--white); margin-right: 10px; vertical-align: middle; }
  .back .brand-sub {
    position: absolute; top: 628px; width: 100%; text-align: center;
    font-family: "Arimo", sans-serif; font-size: 6px; color: var(--white);
  }
  .back .visit {
    position: absolute; top: 666px; width: 100%; text-align: center;
    font-family: "Arimo", sans-serif; font-weight: 700; font-size: 15px; color: var(--white);
  }
  .back .web {
    position: absolute; top: 688px; width: 100%; text-align: center;
    font-family: "Arimo", sans-serif; font-weight: 700; font-size: 14px; color: var(--white); letter-spacing: 3.5px;
  }

  /* Front panel */
  .front { background: var(--black); }
  .front .brand {
    position: absolute; top: 30px; right: 42px;
    font-family: "Arimo", sans-serif; font-weight: 400; font-size: 34px; color: var(--grey-text); letter-spacing: 1px;
  }
  .front .brand .dot { display: inline-block; width: 16px; height: 16px; border-radius: 50%; background: var(--grey-text); margin-right: 10px; vertical-align: middle; }
  .front .brand-sub {
    position: absolute; top: 70px; right: 42px;
    font-family: "Arimo", sans-serif; font-size: 6px; color: var(--grey-text);
  }
  .front .headline {
    position: absolute; top: 510px; left: 0; width: 490px; text-align: center;
    font-family: "Oswald", sans-serif; font-weight: 600; font-size: 70px; line-height: 1; color: var(--ink); letter-spacing: -1px;
  }
  .front .subline {
    position: absolute; top: 586px; left: 0; width: 490px; text-align: center;
    font-family: "Oswald", sans-serif; font-weight: 300; font-size: 40px; line-height: 1; color: var(--ink); letter-spacing: -2px;
  }
  .front .subline .red { color: var(--red); }
  .front .pill {
    position: absolute; top: 634px; left: 152px; width: 188px; height: 40px; border-radius: 20px;
    background: var(--red); color: var(--white); text-align: center;
    font-family: "Arimo", sans-serif; font-weight: 700; font-size: 32px; line-height: 40px; letter-spacing: 1px;
  }
</style>
</head>
<body>
  <main class="flyer">
    <!-- Back cover -->
    <section class="panel back">
      <svg class="shapes" viewBox="0 0 530 750" aria-hidden="true">
        <defs>
          <linearGradient id="backRed" x1="0" y1="0" x2="0" y2="1">
            <stop offset="0" stop-color="#d40f14"/>
            <stop offset="1" stop-color="#a80a0e"/>
          </linearGradient>
          <linearGradient id="edgeFade" gradientUnits="userSpaceOnUse" x1="0" y1="0" x2="530" y2="0">
            <stop offset="0" stop-color="#d40f14" stop-opacity="1"/>
            <stop offset=".35" stop-color="#d40f14" stop-opacity="1"/>
            <stop offset=".75" stop-color="#d40f14" stop-opacity="0"/>
          </linearGradient>
        </defs>
        <path d="M0,398 C30,450 110,478 200,478 C330,476 450,468 530,495 L530,750 L0,750 Z" fill="#1c1c1c"/>
        <path d="M0,398 C30,450 110,478 200,478 C330,476 450,468 530,495" stroke="url(#edgeFade)" stroke-width="4" fill="none"/>
        <path d="M0,600 C80,520 240,470 380,478 C460,484 510,515 530,535 L530,750 L0,750 Z" fill="url(#backRed)"/>
      </svg>
      <h1 class="title">MULOTI</h1>
      <p class="tagline"><span class="red">Create PerformReviseAnalyze</span><span class="dark">&amp;Administrate</span></p>
      <p class="intro">The CREATE-Module letsyou manage your Tasks and Tests easilybyprovidingrepositories in whichtheyreside.&nbsp; By continuously expanding the Task-Repository you can reduce the workload for each new Test you create by being able to reuse and adjus texisting Tasks.<br>At the moment Tasks cancontain the following elements</p>
      <div class="wordcloud" role="img" aria-label="Word cloud graphic centred on the word Strategy with terms like plan, data, sales and process"></div>
      <div class="brand"><span class="dot"></span>MULOTI</div>
      <div class="brand-sub">Create Perform Revise Analyse &amp; Administrate</div>
      <p class="visit">visit us for more information</p>
      <p class="web">-www.yourwebsite.com</p>
    </section>

    <!-- Front cover -->
    <section class="panel front">
      <svg class="shapes" viewBox="0 0 530 750" aria-hidden="true">
        <defs>
          <linearGradient id="paper" x1="0" y1="0" x2="0" y2="1">
            <stop offset="0" stop-color="#ffffff"/>
            <stop offset="1" stop-color="#dcdcdc"/>
          </linearGradient>
          <linearGradient id="photoTone" x1="0" y1="0" x2="1" y2="1">
            <stop offset="0" stop-color="#b9b3a6"/>
            <stop offset=".45" stop-color="#e7e2dc"/>
            <stop offset="1" stop-color="#9fb3cc"/>
          </linearGradient>
        </defs>
        <!-- top right light lobe -->
        <path d="M168,0 C190,50 225,85 300,92 L530,100 L530,0 Z" fill="url(#paper)"/>
        <path d="M168,0 C185,45 215,80 280,92" stroke="#d40f14" stroke-width="4" fill="none"/>
        <!-- red arc framing photo -->
        <path d="M0,108 C90,82 220,90 330,150 C420,200 490,260 530,300 L530,330 C480,285 410,225 320,175 C220,120 90,110 0,128 Z" fill="#d40f14"/>
        <!-- photo area -->
        <path role="img" aria-label="Photo of three colleagues reviewing documents together in a bright office"
              d="M0,122 C90,105 220,115 320,172 C410,222 480,285 530,325 L530,560 C420,470 270,420 140,430 C80,436 30,460 0,485 Z" fill="url(#photoTone)"/>
        <!-- lower black and red swoop -->
        <path d="M0,480 C40,450 90,432 150,428 C280,420 430,480 530,565 L530,600 C430,520 290,455 160,455 C90,455 40,480 0,515 Z" fill="#1c1c1c"/>
        <path d="M0,470 C40,445 90,428 150,424 C280,416 430,470 530,555 L530,568 C430,482 280,428 150,436 C90,440 40,458 0,486 Z" fill="#d40f14"/>
        <!-- text field -->
        <path d="M0,512 C40,480 90,458 160,455 C290,455 430,520 530,600 L530,650 C480,680 400,708 300,712 C200,715 80,700 0,640 Z" fill="url(#paper)"/>
        <!-- bottom red band -->
        <path d="M0,640 C80,700 200,715 300,712 C400,708 480,680 530,650 L530,672 C480,704 400,730 300,733 C200,736 80,720 0,664 Z" fill="#d40f14"/>
      </svg>
      <div class="brand"><span class="dot"></span>MULOTI</div>
      <div class="brand-sub">Create Perform Revise Analyse &amp; Administrate</div>
      <h2 class="headline">MULOTI</h2>
      <p class="subline">IS A WORD <span class="red">PLAY ON</span></p>
      <div class="pill">"ZEBRA"</div>
    </section>
  </main>
</body>
</html>
```